Zielgruppe
Wir machen Softwareentwicklung. Die Zielgruppe sind Geschäftsführer und Leute aus Leitungspositionen aus dem IT Bereich.
Aufgabenstellung
Ich fände es toll, zwei Designs zu haben. Eine etwas seriösere für Geschäftstermine und eine lockere/verspielte für Meetups und Termine an denen ich eher Angestellte suche.
Bitte auch eine Variante mit QR Code.
Die Angaben auf der Visitenkarte sind:
Max Mustermann (Name des Angestellten)
Position
Adresse-Strasse
Adresse-Postleitzahl und Ort
Telefonnummer (bitte keine Fax-Nummer)
Emailadresse
Webadresse

```html
<!DOCTYPE html>
<html lang="de">
<head>
<meta charset="utf-8">
<title>Visitenkarte – Codewerk Nordlicht</title>
<link rel="stylesheet" href="https://fonts.googleapis.com/css2?family=Barlow:wght@400;600&display=swap">
<style>
  :root {
    --bg: #dcdcde;
    --card: #151515;
    --ink: #f2f2f2;
    --muted: #d0d0d0;
    --art-light: #5a5a5a;
    --art-dark: #2e2e2e;
  }
  html, body {
    margin: 0;
    width: 1200px;
    height: 857px;
    overflow: hidden;
    background: var(--bg);
    font-family: "Barlow", Arial, sans-serif;
  }
  .stage {
    position: relative;
    width: 1200px;
    height: 857px;
  }
  .card {
    position: absolute;
    top: 260px;
    width: 520px;
    height: 336px;
    background: var(--card);
    color: var(--ink);
    border-radius: 4px;
    box-shadow: 0 10px 28px rgba(0,0,0,0.18);
    overflow: hidden;
  }
  .card--front { left: 50px; }
  .card--back  { left: 630px; }

  /* Front */
  .brand {
    position: absolute;
    top: 34px;
    right: 70px;
    display: flex;
    align-items: center;
    gap: 14px;
  }
  .brand__dot {
    width: 14px;
    height: 14px;
    border-radius: 50%;
    background: var(--ink);
  }
  .brand__name {
    margin: 0;
    font-size: 40px;
    line-height: 1.02;
    font-weight: 600;
    letter-spacing: 0.01em;
    text-align: right;
    color: var(--ink);
  }
  .brand-artwork {
    position: absolute;
    left: 70px;
    width: 250px;
    top: 150px;
    bottom: 0;
    border-radius: 22px 22px 0 0;
    background: linear-gradient(160deg, var(--art-light) 0%, var(--art-dark) 100%);
  }

  /* Back */
  .corner-artwork {
    position: absolute;
    left: 0;
    top: 0;
    width: 240px;
    height: 128px;
    border-radius: 0 0 26px 0;
    background: linear-gradient(200deg, var(--art-light) 0%, var(--art-dark) 100%);
  }
  .person {
    position: absolute;
    left: 60px;
    top: 176px;
    font-size: 14px;
    line-height: 1.35;
    color: var(--muted);
  }
  .person__name {
    font-size: 18px;
    font-weight: 600;
    color: var(--ink);
    margin: 0 0 2px;
  }
  .person__role { margin: 0 0 14px; }
  .person__address { margin: 0; font-style: normal; }

  .contact {
    position: absolute;
    right: 30px;
    top: 150px;
    list-style: none;
    margin: 0;
    padding: 0;
    font-size: 14px;
    color: var(--ink);
  }
  .contact__item {
    display: flex;
    align-items: center;
    gap: 9px;
    margin-bottom: 7px;
  }
  .contact__icon {
    width: 15px;
    height: 15px;
    fill: none;
    stroke: var(--ink);
    stroke-width: 1.6;
  }
</style>
</head>
<body>
<main class="stage">
  <section class="card card--front">
    <div class="brand">
      <span class="brand__dot"></span>
      <p class="brand__name">Codewerk<br>Nordlicht</p>
    </div>
    <div class="brand-artwork" role="img" aria-label="Markenillustration: stilisierter Roboter in einem abgerundeten Rahmen, weiß auf Schwarz"></div>
  </section>

  <section class="card card--back">
    <div class="corner-artwork" role="img" aria-label="Ausschnitt der Markenillustration als Eckmotiv, weiß auf Schwarz"></div>
    <div class="person">
      <p class="person__name">Max Mustermann</p>
      <p class="person__role">Position</p>
      <address class="person__address">Musterstraße 12<br>21345 Musterstadt</address>
    </div>
    <ul class="contact">
      <li class="contact__item">
        <svg class="contact__icon" viewBox="0 0 16 16"><path d="M3 2l3 1 1 3-2 1.5a8 8 0 0 0 3.5 3.5L10 9l3 1 1 3-2 1C7 14 2 9 2 4z"/></svg>
        <span>012345678901</span>
      </li>
      <li class="contact__item">
        <svg class="contact__icon" viewBox="0 0 16 16"><rect x="1.5" y="3.5" width="13" height="9"/><path d="M1.5 3.5 8 9l6.5-5.5"/></svg>
        <span>mustermann@codewerk-nord.de</span>
      </li>
      <li class="contact__item">
        <svg class="contact__icon" viewBox="0 0 16 16"><circle cx="8" cy="8" r="6.5"/><ellipse cx="8" cy="8" rx="3" ry="6.5"/><path d="M1.5 8h13"/></svg>
        <span>codewerk-nord.de</span>
      </li>
    </ul>
  </section>
</main>
</body>
</html>
```